Redesign our iOS App Design mockups

- Redesign our current Veltro App Mockup
- Keep the design simple so that programmers do not have to do too much extra work to make your design work.
- Look at the attached website screenshot for the overall look and feel, and color scheme
- Convert the attached vector logo to iOS Icon format.
- Deliver all graphics in the density required for Veltro QL Prime.
- I have attached the current iOS mockup in a .ZIP file but you can view it here as well: https://boards.mockvault.net/share/QWTRPL8HNB2

Target Market(s)

Mostly Male Internet Consumers between the ages of 20 and 35

Industry/Entity Type

Internet

Colors

Designer to choose colors to be used in the design.

Requirements
Must have
• - Deliver all graphics in the density required for Veltro QL Prime
• - Should also look good on Tabrix and Tabrix pro
• - Design type should be “FLAT.”
• - Spell out fonts used in the design and where they are used. Also, include font sizes.
• - Please use ALL the elements in each page and use all placements and text EXACTLY. Please do not improvise with text or components.
• I have designed the mockup exactly the way I like it. I just want it to made to look better.
Should not have

```html
<!DOCTYPE html>
<html lang="en">
<head>
<meta charset="utf-8">
<title>NestLink — Splash and Login</title>
<link rel="stylesheet" href="https://fonts.googleapis.com/css2?family=Roboto:wght@400;500&family=Nunito:wght@500;600&display=swap">
<style>
  :root {
    --canvas: #ffffff;
    --screen-white: #ffffff;
    --screen-soft: #f5f6f9;
    --ink: #111318;
    --muted: #8a8d94;
    --label: #9a9ca3;
    --coral: #f15b4f;
    --link: #3d8fe0;
    --field-shadow: rgba(30, 40, 60, 0.06);
    --icon-grey: #b5b7bd;
  }
  * { box-sizing: border-box; margin: 0; padding: 0; }
  html, body { width: 1200px; height: 1200px; overflow: hidden; }
  body {
    background: var(--canvas);
    font-family: "Roboto", Arial, sans-serif;
    position: relative;
  }
  .screen {
    position: absolute;
    top: 174px;
    width: 373px;
    height: 805px;
    border-radius: 34px;
    overflow: hidden;
    box-shadow: 0 20px 50px rgba(0,0,0,0.14);
  }
  .screen--splash { left: 210px; background: var(--screen-white); }
  .screen--login { left: 706px; background: var(--screen-soft); }

  .status-bar {
    position: absolute; top: 0; left: 0; right: 0; height: 48px;
    display: flex; justify-content: space-between; align-items: center;
    padding: 4px 22px 0 35px;
  }
  .status-bar__time { font-size: 15px; font-weight: 500; color: var(--ink); letter-spacing: -0.2px; }
  .status-bar__icons { display: flex; gap: 5px; align-items: center; }

  .brand {
    position: absolute; left: 0; right: 0;
    display: flex; flex-direction: column; align-items: center; gap: 14px;
  }
  .brand__dot { width: 70px; height: 70px; border-radius: 50%; background: var(--coral); }
  .brand__name {
    font-family: "Roboto", Arial, sans-serif;
    font-size: 23px; font-weight: 400; color: var(--ink); letter-spacing: -0.3px;
  }
  .screen--splash .brand { top: 330px; }
  .screen--login .brand { top: 150px; }

  .loading {
    position: absolute; top: 474px; left: 0; right: 0; text-align: center;
    font-family: "Nunito", Arial, sans-serif; font-size: 16px; color: #6f7278;
  }
  .spinner { position: absolute; top: 520px; left: 50%; margin-left: -17px; }

  .home-indicator {
    position: absolute; bottom: 10px; left: 50%; width: 133px; height: 4px;
    margin-left: -66px; border-radius: 2px; background: var(--ink);
  }

  .nav-header {
    position: absolute; top: 0; left: 0; right: 0; height: 87px;
    background: var(--screen-white);
    box-shadow: 0 2px 6px rgba(0,0,0,0.03);
  }
  .nav-header__title {
    position: absolute; top: 56px; left: 0; right: 0; text-align: center;
    font-family: "Nunito", Arial, sans-serif; font-size: 17px; font-weight: 600; color: var(--ink);
  }

  .field-label {
    position: absolute; left: 24px;
    font-size: 14px; color: var(--label);
  }
  .field {
    position: absolute; left: 24px; width: 325px; height: 50px;
    background: var(--screen-white); border-radius: 8px;
    box-shadow: 0 2px 8px var(--field-shadow);
    display: flex; align-items: center; justify-content: space-between;
    padding: 0 14px 0 20px;
    font-size: 15.5px; color: #2a2c31;
  }
  .field--password { letter-spacing: 1px; font-size: 14px; align-items: flex-start; padding-top: 16px; }
  .field--password svg { margin-top: -2px; }

  .forgot-link {
    position: absolute; top: 495px; left: 24px;
    font-size: 13px; font-weight: 500; color: var(--link); text-decoration: underline;
  }
  .primary-button {
    position: absolute; top: 529px; left: 24px; width: 325px; height: 50px;
    border: none; border-radius: 8px; background: var(--coral);
    color: #fff; font-family: "Roboto", Arial, sans-serif; font-size: 17px; font-weight: 500;
    letter-spacing: -0.2px;
    box-shadow: 0 3px 6px rgba(241,91,79,0.25);
  }
  .signup-prompt {
    position: absolute; top: 744px; left: 0; right: 0; text-align: center;
    font-size: 12.5px; color: var(--muted); letter-spacing: -0.2px;
  }
  .signup-prompt a { color: var(--link); font-weight: 500; text-decoration: none; margin-left: 4px; }
</style>
</head>
<body>

  <section class="screen screen--splash">
    <div class="status-bar">
      <span class="status-bar__time">9:41</span>
      <span class="status-bar__icons">
        <svg width="18" height="11" viewBox="0 0 18 11"><rect x="0" y="7" width="3" height="4" rx="1" fill="#111318"/><rect x="5" y="5" width="3" height="6" rx="1" fill="#111318"/><rect x="10" y="2.5" width="3" height="8.5" rx="1" fill="#111318"/><rect x="15" y="0" width="3" height="11" rx="1" fill="#111318"/></svg>
        <svg width="16" height="11" viewBox="0 0 16 11"><path d="M8 10.5 5.6 8a3.4 3.4 0 0 1 4.8 0z" fill="#111318"/><path d="M3.3 5.8a6.6 6.6 0 0 1 9.4 0l-1.3 1.3a4.8 4.8 0 0 0-6.8 0z" fill="#111318"/><path d="M1 3.5a9.9 9.9 0 0 1 14 0l-1.3 1.3a8.1 8.1 0 0 0-11.4 0z" fill="#111318"/></svg>
        <svg width="25" height="12" viewBox="0 0 25 12"><rect x="0.5" y="0.5" width="21" height="11" rx="3" fill="none" stroke="#111318" opacity="0.4"/><rect x="2" y="2" width="18" height="8" rx="1.5" fill="#111318"/><rect x="22.5" y="4" width="1.5" height="4" rx="0.7" fill="#111318" opacity="0.4"/></svg>
      </span>
    </div>

    <div class="brand">
      <span class="brand__dot"></span>
      <span class="brand__name">NESTLINK</span>
    </div>

    <p class="loading">Loading...</p>
    <svg class="spinner" width="34" height="34" viewBox="0 0 34 34" aria-hidden="true">
      <g stroke="#444" stroke-width="2" stroke-linecap="round">
        <line x1="17" y1="3" x2="17" y2="10" opacity="0.15"/>
        <line x1="17" y1="3" x2="17" y2="10" transform="rotate(30 17 17)" opacity="0.2"/>
        <line x1="17" y1="3" x2="17" y2="10" transform="rotate(60 17 17)" opacity="0.25"/>
        <line x1="17" y1="3" x2="17" y2="10" transform="rotate(90 17 17)" opacity="0.3"/>
        <line x1="17" y1="3" x2="17" y2="10" transform="rotate(120 17 17)" opacity="0.4"/>
        <line x1="17" y1="3" x2="17" y2="10" transform="rotate(150 17 17)" opacity="0.5"/>
        <line x1="17" y1="3" x2="17" y2="10" transform="rotate(180 17 17)" opacity="0.6"/>
        <line x1="17" y1="3" x2="17" y2="10" transform="rotate(210 17 17)" opacity="0.7"/>
        <line x1="17" y1="3" x2="17" y2="10" transform="rotate(240 17 17)" opacity="0.8"/>
        <line x1="17" y1="3" x2="17" y2="10" transform="rotate(270 17 17)" opacity="0.9"/>
        <line x1="17" y1="3" x2="17" y2="10" transform="rotate(300 17 17)" opacity="1"/>
        <line x1="17" y1="3" x2="17" y2="10" transform="rotate(330 17 17)" opacity="0.1"/>
      </g>
    </svg>

    <span class="home-indicator"></span>
  </section>

  <section class="screen screen--login">
    <header class="nav-header">
      <div class="status-bar">
        <span class="status-bar__time">9:41</span>
        <span class="status-bar__icons">
          <svg width="18" height="11" viewBox="0 0 18 11"><rect x="0" y="7" width="3" height="4" rx="1" fill="#111318"/><rect x="5" y="5" width="3" height="6" rx="1" fill="#111318"/><rect x="10" y="2.5" width="3" height="8.5" rx="1" fill="#111318"/><rect x="15" y="0" width="3" height="11" rx="1" fill="#111318"/></svg>
          <svg width="16" height="11" viewBox="0 0 16 11"><path d="M8 10.5 5.6 8a3.4 3.4 0 0 1 4.8 0z" fill="#111318"/><path d="M3.3 5.8a6.6 6.6 0 0 1 9.4 0l-1.3 1.3a4.8 4.8 0 0 0-6.8 0z" fill="#111318"/><path d="M1 3.5a9.9 9.9 0 0 1 14 0l-1.3 1.3a8.1 8.1 0 0 0-11.4 0z" fill="#111318"/></svg>
          <svg width="25" height="12" viewBox="0 0 25 12"><rect x="0.5" y="0.5" width="21" height="11" rx="3" fill="none" stroke="#111318" opacity="0.4"/><rect x="2" y="2" width="18" height="8" rx="1.5" fill="#111318"/><rect x="22.5" y="4" width="1.5" height="4" rx="0.7" fill="#111318" opacity="0.4"/></svg>
        </span>
      </div>
      <h1 class="nav-header__title">Login</h1>
    </header>

    <div class="brand">
      <span class="brand__dot"></span>
      <span class="brand__name">NESTLINK</span>
    </div>

    <label class="field-label" style="top:306px;">User ID:</label>
    <div class="field" style="top:330px;">
      <span>email@example.com</span>
      <svg width="14" height="14" viewBox="0 0 14 14" aria-hidden="true"><path d="M1 1l12 12M13 1 1 13" stroke="#9a9ca3" stroke-width="1.4" stroke-linecap="round"/></svg>
    </div>

    <label class="field-label" style="top:398px;">Password:</label>
    <div class="field field--password" style="top:422px;">
      <span>********</span>
      <svg width="26" height="22" viewBox="0 0 26 22" aria-hidden="true">
        <path d="M3 11c3-4 6.5-6 10-6s7 2 10 6c-3 4-6.5 6-10 6s-7-2-10-6z" fill="none" stroke="#b5b7bd" stroke-width="1.3"/>
        <circle cx="13" cy="11" r="3" fill="none" stroke="#b5b7bd" stroke-width="1.3"/>
        <path d="M4 20 22 2" stroke="#b5b7bd" stroke-width="1.3" stroke-linecap="round"/>
      </svg>
    </div>

    <a class="forgot-link" href="#">FORGOT PASSWORD?</a>
    <button class="primary-button" type="button">CONTINUE</button>

    <p class="signup-prompt">Don't have an account yet?<a href="#">Sign up here.</a></p>

    <span class="home-indicator"></span>
  </section>

</body>
</html>
```